I need to refresh my meeting minutes pages (2 of them)

I have 2 pages that need to be modernized with a new look and feel. I have attached the 2 pages that need the refresh. I am okay with one page submissions as long as the winner is willing to add the second page before payment :-) Any questions please let me know. The logo on the page is not ours but a sample of what client may give us.

```html
<!DOCTYPE html>
<html lang="en">
<head>
<meta charset="utf-8">
<title>Board Meetings Portal</title>
<link href="https://fonts.googleapis.com/css2?family=Figtree:wght@400;500;600;700&display=swap" rel="stylesheet">
<style>
  :root{
    --bg-deep:#0a4418;
    --green:#156f31;
    --green-dark:#0c4a1d;
    --green-row:#0f5724;
    --gold:#c9a400;
    --gold-text:#c9a400;
    --main-bg:#f1f6f2;
    --white:#ffffff;
    --ink:#111;
    --track:#dfe8e1;
    --thumb:#b7cbbd;
  }
  *{box-sizing:border-box;margin:0;padding:0}
  html,body{width:997px;height:1200px;overflow:hidden}
  body{background:var(--bg-deep);font-family:'Figtree',sans-serif;position:relative;color:var(--ink)}
  .screen{position:absolute;left:52px;width:893px;display:flex;box-shadow:0 10px 30px rgba(0,0,0,.35)}
  .screen--meetings{top:57px;height:502px}
  .screen--agenda{top:607px;height:513px}
  .sidebar{width:209px;background:var(--green);color:var(--white);flex:none;overflow:hidden}
  .brand{height:113px;display:flex;flex-direction:column;align-items:center;justify-content:center;text-align:center}
  .brand-name{font-weight:700;font-size:13px;line-height:1.25;color:var(--white)}
  .menu-head{height:25px;display:flex;align-items:center;justify-content:space-between;padding:0 9px;font-weight:700;font-size:9.5px;background:var(--green-dark);letter-spacing:.1px}
  .menu-head--open{background:var(--gold)}
  .menu-head svg{width:8px;height:8px}
  .meeting-list{padding-top:4px}
  .meeting{height:29px;padding:4px 9px 0;position:relative}
  .meeting--active{background:var(--green-dark);border-left:3px solid var(--gold);padding-left:6px}
  .meeting-date{font-weight:600;font-size:9px;line-height:1.2}
  .meeting-type{font-size:6px;opacity:.9}
  .meeting .star{position:absolute;right:9px;top:8px;width:11px;height:11px}
  .sub-item{height:20px;display:flex;align-items:center;justify-content:space-between;padding:0 9px;font-size:7px}
  .sub-item--active{background:var(--green-dark);border-left:3px solid var(--gold);padding-left:6px;height:23px}
  .sub-item svg{width:9px;height:9px}
  .sub-list{padding:1px 0 7px}
  .main{flex:1;background:var(--main-bg);position:relative}
  .search{position:absolute;left:33px;top:35px;width:232px;height:37px;border:1px solid var(--green);border-radius:3px;background:var(--white);display:flex;align-items:center;padding-left:10px;gap:5px;font-size:11px;color:#8a8a8a}
  .search svg{width:11px;height:11px}
  .tabs{position:absolute;top:35px;left:356px;display:flex;gap:14px}
  .tab{height:37px;background:var(--white);border-radius:3px;display:flex;align-items:center;justify-content:center;font-size:11.5px;padding:0 12px}
  .tab--on{background:var(--green);color:var(--white);font-weight:600;box-shadow:0 2px 5px rgba(0,0,0,.2)}
  .pager{position:absolute;top:113px;left:33px;display:flex;gap:6px}
  .round{width:26px;height:26px;border-radius:50%;background:var(--white);display:flex;align-items:center;justify-content:center;box-shadow:0 1px 4px rgba(0,0,0,.08)}
  .round--fill{background:var(--green)}
  .round svg{width:11px;height:11px}
  .card{position:absolute;left:33px;top:152px;width:628px;background:var(--white);border-radius:4px;padding:16px 19px}
  .card-title{color:var(--green);font-weight:700;font-size:17px}
  .date-pill{display:inline-block;margin-top:6px;background:var(--gold);color:var(--white);font-size:10px;padding:3px 7px;border-radius:10px}
  .address{margin-top:13px;font-size:10px;line-height:14px}
  .notice{margin-top:12px;font-size:9.5px;font-weight:600;line-height:12px}
  .actions{margin-top:17px;display:flex;gap:20px;padding-bottom:17px}
  .btn{height:35px;border-radius:18px;border:1px solid var(--green);color:var(--green);display:flex;align-items:center;gap:5px;padding:0 11px;font-weight:600;font-size:11px;background:var(--white)}
  .btn--solid{background:var(--green);color:var(--white)}
  .btn svg{width:12px;height:12px}
  .scroll-track{position:absolute;left:3px;top:113px;width:6px;height:364px;background:var(--track);border-radius:3px}
  .scroll-thumb{width:6px;height:186px;background:var(--thumb);border-radius:3px}
  .details{margin-top:10px;display:grid;grid-template-columns:73px auto;row-gap:7px;font-size:10.5px;line-height:14px}
  .details dd{color:var(--gold-text);font-weight:600}
  .file-btn{margin-top:16px;display:inline-flex;height:35px;align-items:center;gap:5px;padding:0 12px;background:var(--green);color:var(--white);font-weight:600;font-size:11px;border-radius:18px}
  .file-btn svg{width:12px;height:12px}
  .card--agenda{height:252px}
</style>
</head>
<body>

<section class="screen screen--meetings">
  <aside class="sidebar">
    <div class="brand"><span class="brand-name">Oakridge City<br>School District</span></div>
    <div class="menu-head">FEATURUED <svg viewBox="0 0 10 10"><path d="M2 3.5l3 3 3-3" fill="none" stroke="#fff" stroke-width="1.4"/></svg></div>
    <div class="menu-head menu-head--open">2025 <svg viewBox="0 0 10 10"><path d="M2 6.5l3-3 3 3" fill="none" stroke="#fff" stroke-width="1.4"/></svg></div>
    <div class="meeting-list">
      <div class="meeting"><div class="meeting-date">May 1, 2025 (Thu)</div><div class="meeting-type">Special Meeting Agenda</div>
        <svg class="star" viewBox="0 0 24 24"><path d="M12 2l3 6.5 7 .8-5.2 4.8 1.4 7L12 17.6 5.8 21.1l1.4-7L2 9.3l7-.8z" fill="#e8c200"/></svg></div>
      <div class="meeting meeting--active"><div class="meeting-date">Apr 24, 2025 (Thu)</div><div class="meeting-type">Regular Meeting Agenda</div></div>
      <div class="meeting"><div class="meeting-date">Apr 10, 2025 (Thu)</div><div class="meeting-type">Regular Meeting Agenda</div></div>
      <div class="meeting"><div class="meeting-date">Mar 20, 2025 (Thu)</div><div class="meeting-type">Regular Meeting Agenda</div></div>
      <div class="meeting"><div class="meeting-date">Mar 17, 2025 (Thu)</div><div class="meeting-type">Special Meeting Agenda</div></div>
      <div class="meeting"><div class="meeting-date">Mar 12, 2025 (Thu)</div><div class="meeting-type">Special Meeting Agenda</div></div>
      <div class="meeting"><div class="meeting-date">Mar 6, 2025 (Thu)</div><div class="meeting-type">Regular Meeting Agenda</div></div>
      <div class="meeting"><div class="meeting-date">Feb 26, 2025 (Wed)</div><div class="meeting-type">Special Meeting Agenda - Cancelled</div></div>
      <div class="meeting"><div class="meeting-date">Feb 20, 2025 (Thu)</div><div class="meeting-type">Regular Meeting Agenda</div></div>
      <div class="meeting"><div class="meeting-date">Feb 6, 2025 (Thu)</div><div class="meeting-type">Regular Meeting Agenda</div></div>
      <div class="meeting"><div class="meeting-date">Feb 3, 2025 (Thu)</div><div class="meeting-type">Special Meeting Agenda</div></div>
    </div>
  </aside>
  <main class="main">
    <div class="scroll-track"><div class="scroll-thumb"></div></div>
    <div class="search"><svg viewBox="0 0 24 24"><circle cx="10.5" cy="10.5" r="7" fill="none" stroke="#156f31" stroke-width="2.2"/><path d="M16 16l5 5" stroke="#156f31" stroke-width="2.2"/></svg>Search Meetings</div>
    <nav class="tabs">
      <div class="tab">Featured</div><div class="tab tab--on">Meetings</div><div class="tab">Agenda</div><div class="tab">Policies</div>
    </nav>
    <div class="pager">
      <div class="round"><svg viewBox="0 0 12 12"><path d="M7.5 2L3.5 6l4 4" fill="none" stroke="#156f31" stroke-width="1.6"/></svg></div>
      <div class="round"><svg viewBox="0 0 12 12"><path d="M4.5 2l4 4-4 4" fill="none" stroke="#156f31" stroke-width="1.6"/></svg></div>
    </div>
    <article class="card">
      <h1 class="card-title">Regular Meeting Agenda</h1>
      <span class="date-pill">Thursday, April 24, 2025</span>
      <p class="address">Westbrook High School Media Center,<br>1,800 North Maple Grove Road,<br>Oakridge, Ohio 44000<br>6:00 P.M.</p>
      <p class="notice">This meeting is a &nbsp;meeting of the Board of Education in public for the purpose of conducting the District’s business.<br>There is a time for public participation during the meeting as indicated in the agenda.</p>
      <div class="actions">
        <div class="btn btn--solid"><svg viewBox="0 0 24 24"><rect x="5" y="3" width="14" height="18" rx="1.5" fill="none" stroke="#e8c200" stroke-width="1.8"/><path d="M8.5 8h7M8.5 12h7M8.5 16h5" stroke="#e8c200" stroke-width="1.6"/></svg>View the Agenda</div>
        <div class="btn"><svg viewBox="0 0 24 24"><path d="M6 2.5h8l5 5V21.5H6z" fill="none" stroke="#c9a400" stroke-width="1.6"/><path d="M14 2.5v5h5" fill="none" stroke="#c9a400" stroke-width="1.6"/></svg>Download Agenda as PDF</div>
        <div class="btn"><svg viewBox="0 0 24 24"><rect x="7" y="3" width="10" height="5" fill="none" stroke="#c9a400" stroke-width="1.6"/><rect x="3" y="8" width="18" height="9" rx="2" fill="none" stroke="#c9a400" stroke-width="1.6"/><rect x="7" y="14" width="10" height="7" fill="#fff" stroke="#c9a400" stroke-width="1.6"/></svg>Print the Agenda</div>
      </div>
    </article>
  </main>
</section>

<section class="screen screen--agenda">
  <aside class="sidebar">
    <div class="brand"><span class="brand-name">Oakridge City<br>School District</span></div>
    <div class="menu-head">*R* WELCOME <svg viewBox="0 0 10 10"><path d="M2 3.5l3 3 3-3" fill="none" stroke="#fff" stroke-width="1.4"/></svg></div>
    <div class="menu-head" style="background:var(--green-row)">*R* CALL TO ORDER <svg viewBox="0 0 10 10"><path d="M2 3.5l3 3 3-3" fill="none" stroke="#fff" stroke-width="1.4"/></svg></div>
    <div class="menu-head">*R* OAKRIDGE PROUD <svg viewBox="0 0 10 10"><path d="M2 3.5l3 3 3-3" fill="none" stroke="#fff" stroke-width="1.4"/></svg></div>
    <div class="menu-head menu-head--open">*R* INFORMATION TO THE BOARD <svg viewBox="0 0 10 10"><path d="M2 6.5l3-3 3 3" fill="none" stroke="#fff" stroke-width="1.4"/></svg></div>
    <div class="sub-list">
      <div class="sub-item">Superintendent - ACES / PAGE / First Step</div>
      <div class="sub-item">ACES</div>
      <div class="sub-item sub-item--active">PAGE <svg viewBox="0 0 24 24"><rect x="5" y="3" width="14" height="18" rx="1.5" fill="none" stroke="#e8c200" stroke-width="1.8"/><path d="M8.5 8h7M8.5 12h7M8.5 16h5" stroke="#e8c200" stroke-width="1.6"/></svg></div>
      <div class="sub-item">First Step</div>
    </div>
    <div class="menu-head">*R* COMMUNICATION(S) <svg viewBox="0 0 10 10"><path d="M2 3.5l3 3 3-3" fill="none" stroke="#fff" stroke-width="1.4"/></svg></div>
    <div class="menu-head" style="background:var(--green-row)">*R* PUBLIC PARTICIPATION <svg viewBox="0 0 10 10"><path d="M2 3.5l3 3 3-3" fill="none" stroke="#fff" stroke-width="1.4"/></svg></div>
    <div class="menu-head">ADOPTION OF AMENDMENTS <svg viewBox="0 0 10 10"><path d="M2 3.5l3 3 3-3" fill="none" stroke="#fff" stroke-width="1.4"/></svg></div>
  </aside>
  <main class="main">
    <div class="search"><svg viewBox="0 0 24 24"><circle cx="10.5" cy="10.5" r="7" fill="none" stroke="#156f31" stroke-width="2.2"/><path d="M16 16l5 5" stroke="#156f31" stroke-width="2.2"/></svg>Search Agenda</div>
    <nav class="tabs">
      <div class="tab">Featured</div><div class="tab">Meetings</div><div class="tab tab--on">Agenda</div><div class="tab">Policies</div>
    </nav>
    <div class="pager">
      <div class="round"><svg viewBox="0 0 12 12"><path d="M7.5 2L3.5 6l4 4" fill="none" stroke="#156f31" stroke-width="1.6"/></svg></div>
      <div class="round"><svg viewBox="0 0 12 12"><path d="M4.5 2l4 4-4 4" fill="none" stroke="#156f31" stroke-width="1.6"/></svg></div>
      <div class="round round--fill"><svg viewBox="0 0 24 24"><rect x="7" y="3" width="10" height="5" fill="none" stroke="#fff" stroke-width="1.8"/><rect x="3" y="8" width="18" height="9" rx="2" fill="none" stroke="#fff" stroke-width="1.8"/><rect x="7" y="14" width="10" height="7" fill="#156f31" stroke="#fff" stroke-width="1.8"/></svg></div>
    </div>
    <article class="card card--agenda">
      <h1 class="card-title">Agenda Item Details</h1>
      <dl class="details">
        <dt>Meeting</dt><dd>Apr 10, 2025 – Regular Meeting Agenda</dd>
        <dt>Category</dt><dd>*R* INFORMATION TO THE BOARD</dd>
        <dt>Subject</dt><dd>PAGE</dd>
        <dt>Type</dt><dd></dd>
      </dl>
      <div class="file-btn"><svg viewBox="0 0 24 24"><path d="M6 2.5h8l5 5V21.5H6z" fill="none" stroke="#e8c200" stroke-width="1.6"/><path d="M14 2.5v5h5" fill="none" stroke="#e8c200" stroke-width="1.6"/></svg>2025-04-10 &nbsp;- Oakridge Proud - PAGE &nbsp;(1) .pdf (40 KB)</div>
    </article>
  </main>
</section>

</body>
</html>
```